Plumbing Products Website

This project is to create a web page for Mr. Clear Brook and Mr. Hot Kettle's product offerings. There are 14 unique products. The main page will showcase all 14 products arranged in a clean, concise format that flows nicely and is easy to read.
Furthermore, I need a unique page for each of the 14 products that the main page can link the products to so visitors can click each of them to "Learn More".
For reference, our websites are MrBrookly.example and TopBoilerHub.example; so keep the branding, color-scheme, header, footer, etc. consistent with MrBrookly.example and TopBoilerHub.example.
For reference, here is the catalog. Feel free to copy as much of the content as necessary to build the pages:
https://catalogs.pagefolio.example/MrHotKettle/qvtx/
For clarification, the products are:
1. Whole House Water Purification System
2. Whole House Water Ionization System
3. Whole House Water Softener System
4. Water Heater Sediment Pre-Filter
5. Whole-House UV Water Sterilization System
6. The ULTIMATE Whole House Water Treatment System
7. Under-Sink Reverse Osmosis System with UV Sterilizer
8. Smart Water Heater Regulator with Automated Stand-By for Power Savings
9. Whole House Water Pressure Booster
10. Hot Water Heater Tank Volume Booster
11. Leak Detector with Automatic Water Shutoff
12. Whole House UV Air Purification System
13. Leak Detector Alarm with Mobile App
14. Multi-Gas Detector for Carbon Monoxide, Natural Gas, Propane, Methane, Explosive Gasses, Smoke & Fire
Unfortunately, all the content was created by AI, so I don't have any "original" images or other media. I have attached the logos for your reference though. Also, each individual catalog page is attached.
Once the winning design is chosen, I will need the pages coded and hosted on a staging server for me to view in a live environment before I move them to my server.
Let me know if you have any questions.

```html
<!DOCTYPE html>
<html lang="en">
<head>
<meta charset="utf-8">
<title>Whole House Water Purification System — Mr. Clear Brook</title>
<link rel="stylesheet" href="https://fonts.googleapis.com/css2?family=Inter:wght@400;500;600;700;800&display=swap">
<style>
:root{
  --navy:#0f2444;
  --navy-deep:#0a1a33;
  --blue:#3a7fe0;
  --blue-dark:#1d4fa8;
  --blue-text:#2366c4;
  --green:#2fae4f;
  --ink:#141a24;
  --muted:#6b7380;
  --line:#b9cde6;
  --pale:#e9eff7;
  --white:#ffffff;
}
*{box-sizing:border-box;margin:0;padding:0}
html,body{width:1200px;height:3542px;overflow:hidden}
body{font-family:"Inter",sans-serif;color:var(--ink);background:var(--white)}
.wrap{width:950px;margin:0 auto;position:relative}

/* top bar */
.topbar{height:48px;background:var(--navy);color:#e6ecf5;font-size:13px}
.topbar .wrap{display:flex;justify-content:flex-end;align-items:center;height:48px;gap:46px}
.topbar span{display:flex;align-items:center;gap:10px}

/* nav */
.nav{height:100px;background:var(--white)}
.nav .wrap{display:flex;align-items:center;height:100px}
.brand{display:flex;align-items:center;gap:8px;font-weight:800;font-size:15px;color:var(--navy);width:262px}
.brand i{width:22px;height:22px;border-radius:50%;background:var(--blue);display:block}
.menu{display:flex;gap:38px;font-size:14px;font-weight:500}
.nav .cta{margin-left:auto;background:var(--blue);color:#fff;font-size:12.5px;font-weight:600;width:136px;height:52px;border-radius:13px;display:flex;align-items:center;justify-content:center}

/* hero */
.hero{height:627px;background:radial-gradient(ellipse at 78% 55%,#1d6fb8 0%,#0d3c6e 30%,#06182e 65%,#02070f 100%);color:#fff;position:relative;overflow:hidden}
.hero .wrap{height:627px}
.tag{position:absolute;top:94px;left:0;border:1px solid #c9d3e0;border-radius:16px;padding:8px 22px;font-size:11.5px;font-weight:500;background:rgba(255,255,255,.08)}
.hero h1{position:absolute;top:156px;left:0;font-size:41px;line-height:53px;font-weight:700;width:460px}
.hero p{position:absolute;top:275px;left:0;font-size:11.5px;line-height:18px;width:350px;color:#d7dfeb}
.hero .btns{position:absolute;top:393px;left:0;display:flex;gap:16px}
.btn{height:61px;border-radius:12px;display:flex;align-items:center;justify-content:center;font-size:14px;font-weight:700}
.btn.solid{background:var(--blue);width:148px}
.btn.ghost{border:1.5px solid #e3e9f1;width:238px}
.stats{position:absolute;top:480px;left:0;display:flex;gap:34px}
.stats b{display:block;font-size:17px;font-weight:700;margin-bottom:9px}
.stats small{font-size:12.5px;color:#e4e9f1}
.stars{color:#f5c518;font-size:12px;letter-spacing:2px}
.product-art{position:absolute;left:521px;top:44px;width:400px;height:583px;border-radius:200px 200px 0 0;background:radial-gradient(ellipse at 50% 50%,#4fc3f0 0%,#1b7fd0 35%,rgba(10,50,100,.2) 75%,transparent 100%)}

/* section headings */
.eyebrow{font-size:13px;font-weight:600;letter-spacing:.4px;color:var(--blue-text);text-align:center;text-transform:uppercase}
.title{text-align:center;font-weight:600;font-size:30px}
.lede{text-align:center;font-size:13.5px;color:var(--muted)}

/* features */
.features{height:875px;padding-top:76px}
.features .title{margin-top:14px}
.features .lede{margin-top:20px}
.feature-grid{display:grid;grid-template-columns:repeat(3,299px);gap:28px 26px;margin-top:38px}
.feature{height:278px;border:1.3px solid var(--line);border-radius:20px;padding:32px 24px 0}
.feature .ico{width:72px;height:72px;border-radius:14px;background:#eef3fb;display:flex;align-items:center;justify-content:center}
.feature h3{font-size:18px;font-weight:600;margin-top:28px}
.feature p{font-size:12.5px;line-height:18px;color:var(--muted);margin-top:14px;width:230px}
.feature a{display:block;font-size:12.5px;font-weight:600;color:var(--blue-dark);margin-top:22px;text-decoration:none}

/* contaminants */
.contam{height:398px;background:var(--pale);padding-top:61px}
.contam .title{color:var(--blue-dark);font-size:32px;margin-top:14px}
.contam .lede{margin-top:10px;font-size:14px}
.contam-grid{display:grid;grid-template-columns:repeat(4,212px);gap:34px;margin-top:44px}
.contam-card{height:149px;background:#fff;border:1px solid #d3dfee;border-radius:10px;text-align:center;padding-top:20px}
.contam-card .ring{width:62px;height:62px;border-radius:50%;background:#eef2f8;margin:0 auto;display:flex;align-items:center;justify-content:center}
.contam-card h4{color:var(--blue-dark);font-size:15px;font-weight:600;margin-top:14px}
.contam-card small{display:block;font-size:11px;color:#9aa2ad;margin-top:6px}

/* pair */
.pair{height:358px;padding-top:61px}
.pair .title{font-size:27px}
.pair-grid{display:grid;grid-template-columns:repeat(3,299px);gap:26px;margin-top:40px}
.pair-card{height:157px;border:1.3px solid var(--line);border-radius:20px;padding:22px 29px 0}
.pair-card em{font-style:normal;font-size:10.5px;font-weight:600;color:var(--blue-dark)}
.pair-card h4{font-size:16px;font-weight:600;line-height:24px;margin-top:12px}
.pair-card a{display:block;font-size:12px;color:var(--ink);margin-top:12px;text-decoration:none}

/* zip band */
.zip{height:251px;background:linear-gradient(90deg,#1b58ad 0%,#2a86d8 100%);color:#fff;text-align:center;padding-top:50px}
.zip h2{font-size:31px;font-weight:600}
.zip p{font-size:13.5px;margin-top:14px}
.zip form{display:flex;justify-content:center;gap:19px;margin-top:26px}
.zip .field{width:291px;height:62px;background:#fff;border-radius:12px;color:#9aa2ad;font-size:15px;display:flex;align-items:center;padding-left:24px;text-align:left}
.zip .go{width:166px;height:62px;background:var(--green);border-radius:12px;font-size:15px;font-weight:600;display:flex;align-items:center;justify-content:center}

/* consult */
.consult{height:580px;padding-top:76px}
.consult-card{height:437px;display:flex;border-radius:18px;box-shadow:0 6px 24px rgba(15,36,68,.08);background:#fff}
.consult-photo{width:476px;height:437px;border-radius:18px;background:linear-gradient(135deg,#e4e2de 0%,#cfc9c2 45%,#8a7f76 75%,#e8e6e3 100%)}
.consult-form{margin-left:33px;width:407px;padding-top:24px;font-size:12px}
.consult-form label{display:block;font-weight:500;margin-bottom:14px}
.consult-form .input{height:50px;border:1px solid #b8c0cb;border-radius:11px;display:flex;align-items:center;padding-left:18px;font-size:11.5px;color:#6b7380;margin-bottom:20px}
.consult-form .input.value{color:var(--ink)}
.row{display:grid;grid-template-columns:187px 187px;gap:33px}
.submit{height:68px;background:var(--green);color:#fff;border-radius:12px;display:flex;align-items:center;justify-content:center;font-weight:600;font-size:12px;margin-top:-4px}
.fine{font-size:10px;line-height:20px;color:#6b7380;text-align:center;margin-top:10px}

/* footer */
.footer{height:305px;background:var(--navy-deep);color:#dfe6f0}
.footer .inner{width:994px;margin:0 auto;position:relative;height:305px}
.footer .cols{display:flex;padding-top:54px}
.footer .about{width:305px}
.footer .about b{font-size:16px;font-weight:800;color:#fff}
.footer .about p{font-size:11.5px;line-height:18px;color:#aebbd0;margin-top:12px;width:245px}
.footer .col{width:227px;font-size:11.5px}
.footer .col h5{font-size:12px;font-weight:700;letter-spacing:.6px;color:#fff;margin-bottom:16px}
.footer .col div{margin-bottom:13px}
.footer .base{position:absolute;left:0;right:0;bottom:0;height:40px;border-top:1px solid #27395a;display:flex;justify-content:space-between;align-items:center;font-size:10.5px;color:#9aa8bd}
</style>
</head>
<body>

<div class="topbar">
  <div class="wrap">
    <span><svg width="14" height="14" viewBox="0 0 24 24" fill="#fff"><path d="M6.6 10.8a15.5 15.5 0 0 0 6.6 6.6l2.2-2.2a1 1 0 0 1 1-.25 11.4 11.4 0 0 0 3.6.57 1 1 0 0 1 1 1V20a1 1 0 0 1-1 1A17 17 0 0 1 3 4a1 1 0 0 1 1-1h3.5a1 1 0 0 1 1 1c0 1.25.2 2.45.57 3.6a1 1 0 0 1-.25 1z"/></svg>(555) 014-2290</span>
    <span><svg width="16" height="12" viewBox="0 0 16 12"><rect width="16" height="12" rx="2" fill="#fff"/><path d="M1 1l7 5 7-5" stroke="#0f2444" stroke-width="1.4" fill="none"/></svg>info@topboilerhub.example</span>
  </div>
</div>

<header class="nav">
  <div class="wrap">
    <div class="brand"><i></i>Mr. Hot Kettle</div>
    <nav class="menu"><span>Home</span><span>Products</span><span>About</span><span>Testimonial's</span><span>Contact</span></nav>
    <div class="cta">Get Free Quote</div>
  </div>
</header>

<section class="hero">
  <div class="wrap">
    <div class="tag">WATER TREATMENT</div>
    <h1>Whole House Water Purification System</h1>
    <p>Clean, great-tasting water at every tap in your home — filtered at the source, installed by professionals, backed by a lifetime warranty.</p>
    <div class="btns"><div class="btn solid">Get Quote</div><div class="btn ghost">Call (555) 014-2290</div></div>
    <div class="stats">
      <div><b>27+ yrs</b><small>serving Arizona</small></div>
      <div><b>4.9 / 5</b><span class="stars">★★★★★</span></div>
      <div><b>60-min</b><small>emergency response</small></div>
    </div>
    <div class="product-art" role="img" aria-label="Filter cartridge wrapped in a swirling splash of blue water"></div>
  </div>
</section>

<section class="features">
  <div class="wrap">
    <div class="eyebrow">Full-Service Cleaning</div>
    <h2 class="title">Every surface, handled by pros</h2>
    <p class="lede">Truck-mounted, certified cleaning for every room and surface — expanding all the time.</p>
    <div class="feature-grid">
      <div class="feature"><div class="ico"><svg width="24" height="24" viewBox="0 0 24 24"><rect x="2" y="2" width="20" height="20" rx="4" fill="#2b6fd6"/><path d="M7 10h10M7 14h6" stroke="#fff" stroke-width="1.8"/></svg></div><h3>Complete System Included</h3><p>High-performance filter, housing, mounting bracket and all parts needed for install.</p><a>Learn more →</a></div>
      <div class="feature"><div class="ico"><svg width="24" height="24" viewBox="0 0 24 24"><path d="M12 2l8 3v6c0 5-3.5 9-8 11-4.5-2-8-6-8-11V5z" fill="#2b6fd6"/><path d="M12 8l1.2 2.4 2.6.4-1.9 1.8.5 2.6L12 14l-2.4 1.2.5-2.6-1.9-1.8 2.6-.4z" fill="#fff"/></svg></div><h3>Professional Installation</h3><p>Installed by experienced, licensed technicians for lasting, reliable performance.</p><a>Learn more →</a></div>
      <div class="feature"><div class="ico"><svg width="26" height="26" viewBox="0 0 24 24"><circle cx="12" cy="12" r="10" fill="#2b6fd6"/><path d="M7.5 12.3l3 3 6-6" stroke="#fff" stroke-width="2" fill="none"/></svg></div><h3>System Check &amp; Testing</h3><p>We test your water and your system on-site to confirm everything is working perfectly.</p><a>Learn more →</a></div>
      <div class="feature"><div class="ico"><svg width="26" height="26" viewBox="0 0 24 24"><circle cx="12" cy="12" r="10" fill="#2b6fd6"/><text x="12" y="17" text-anchor="middle" font-family="Inter,sans-serif" font-size="14" font-weight="700" fill="#fff">$</text></svg></div><h3>Upfront Pricing</h3><p>No surprises on install day. One low price includes everything, start to finish.</p><a>Learn more →</a></div>
      <div class="feature"><div class="ico"><svg width="26" height="24" viewBox="0 0 26 24"><path d="M5 10l3-6h10l3 6z" fill="#2b6fd6"/><rect x="2" y="10" width="22" height="3" rx="1.5" fill="#2b6fd6"/><circle cx="8" cy="17" r="3" fill="#2b6fd6"/><circle cx="18" cy="17" r="3" fill="#2b6fd6"/></svg></div><h3>Lifetime Warranty</h3><p>We stand behind our work and your satisfaction for as long as you own your home.</p><a>Learn more →</a></div>
      <div class="feature"><div class="ico"><svg width="24" height="24" viewBox="0 0 24 24"><path d="M20 3C10 3 3 7 3 14a7 7 0 0 0 14 0c0-4 1-8 3-11z" fill="#2b6fd6"/></svg></div><h3>Clean Water In Every Tap</h3><p>Purifies water at the main line, so the whole home benefits — not just one faucet.</p><a>Learn more →</a></div>
    </div>
  </div>
</section>

<section class="contam">
  <div class="wrap">
    <div class="eyebrow">What's hiding in your water?</div>
    <h2 class="title">Contaminants This System Targets</h2>
    <p class="lede">See what your current water may be carrying — and what gets filtered out.</p>
    <div class="contam-grid">
      <div class="contam-card"><div class="ring"><svg width="30" height="26" viewBox="0 0 30 26" fill="#1e2b3c"><rect x="3" y="3" width="24" height="2"/><rect x="5" y="8" width="3" height="3"/><rect x="11" y="8" width="3" height="3"/><rect x="17" y="8" width="3" height="3"/><rect x="23" y="8" width="3" height="3"/><circle cx="7" cy="16" r="1.5"/><circle cx="13" cy="16" r="1.5"/><circle cx="19" cy="16" r="1.5"/><circle cx="10" cy="21" r="1.5"/><circle cx="16" cy="21" r="1.5"/><circle cx="22" cy="21" r="1.5"/></svg></div><h4>Sediment</h4><small>Dirt, sand &amp; silt</small></div>
      <div class="contam-card"><div class="ring"><svg width="28" height="32" viewBox="0 0 28 32" fill="none" stroke="#1e2b3c" stroke-width="1.6"><path d="M14 2c6 8 11 13 11 19a11 11 0 0 1-22 0c0-6 5-11 11-19z"/><circle cx="14" cy="21" r="6"/><text x="14" y="24" text-anchor="middle" font-family="Inter,sans-serif" font-size="8" font-weight="700" fill="#1e2b3c" stroke="none">Cl</text></svg></div><h4>Chlorine</h4><small>Taste &amp; odor</small></div>
      <div class="contam-card"><div class="ring"><svg width="28" height="28" viewBox="0 0 28 28" fill="none" stroke="#1e2b3c" stroke-width="2"><rect x="6" y="6" width="16" height="16"/><rect x="3" y="3" width="6" height="6" fill="#1e2b3c"/><rect x="19" y="3" width="6" height="6" fill="#1e2b3c"/><rect x="3" y="19" width="6" height="6" fill="#1e2b3c"/><rect x="19" y="19" width="6" height="6" fill="#1e2b3c"/></svg></div><h4>Heavy Metals</h4><small>Lead, mercury &amp; iron</small></div>
      <div class="contam-card"><div class="ring"><svg width="28" height="28" viewBox="0 0 28 28" fill="none" stroke="#1e2b3c" stroke-width="1.6"><path d="M16 3l4 4-12 12-4 1 1-4z"/><circle cx="21" cy="21" r="3"/><path d="M12 20l3 3"/></svg></div><h4>Rust &amp; Corrosion</h4><small>Pipe buildup</small></div>
    </div>
  </div>
</section>

<section class="pair">
  <div class="wrap">
    <h2 class="title">Pair it With</h2>
    <div class="pair-grid">
      <div class="pair-card"><em>WATER TREATMENT</em><h4>The ULTIMATE Whole House Water Treatment System</h4><a>Learn More →</a></div>
      <div class="pair-card"><em>WATER TREATMENT</em><h4>Whole-House UV Water Sterilization System</h4><a>Learn More →</a></div>
      <div class="pair-card"><em>WATER TREATMENT</em><h4>Whole House Water Softener System and UV</h4><a>Learn More →</a></div>
    </div>
  </div>
</section>

<section class="zip">
  <h2>Serving Home &amp; Business across Arizona</h2>
  <p>Enter your zip code to confirm we're in tour area and see local availability</p>
  <form><div class="field">Enter Your zip code</div><div class="go">Check My Area</div></form>
</section>

<section class="consult">
  <div class="wrap">
    <div class="consult-card">
      <div class="consult-photo" role="img" aria-label="Technician pouring a glass of filtered water for a homeowner in a bright kitchen"></div>
      <div class="consult-form">
        <label>Service Needed</label>
        <div class="input value">Carpet Clening</div>
        <div class="row">
          <div><label>Name</label><div class="input">Full Name</div></div>
          <div><label>Zip Code</label><div class="input">8547</div></div>
        </div>
        <div class="row">
          <div><label>Phone</label><div class="input">(58) 855 855</div></div>
          <div><label>Prepare Date</label><div class="input">dd/mm/yyyy</div></div>
        </div>
        <div class="submit">Request a Consultation →</div>
        <p class="fine">By submitting this form, you agree to be contacted by a Clearline representative regarding your project inquiry.</p>
      </div>
    </div>
  </div>
</section>

<footer class="footer">
  <div class="inner">
    <div class="cols">
      <div class="about"><b>Mr. Clear Brook</b><p>Whole-home water treatment, water heater, and safety systems installed by licensed professionals across South Florida.</p></div>
      <div class="col"><h5>COMPANY</h5><div>Home</div><div>About Us</div><div>All Products</div><div>Testimonials</div><div>Contact Us</div></div>
      <div class="col"><h5>CATEGORIES</h5><div>Water Treatment</div><div>Water Heater Upgrades</div><div>Leak &amp; Air Safety</div></div>
      <div class="col"><h5>CONTACT US</h5><div>(555) 014-2290</div><div>info@topboilerhub.example</div><div>2200 Cedar Loop, Suite 4<br>Lakeview, FL 33000</div></div>
    </div>
    <div class="base"><span>Copyright © 2026 Mr. Clear Brook. All Rights Reserved.</span><span>Privacy Policy · Terms of Use · Sitemap</span></div>
  </div>
</footer>

</body>
</html>
```